Small business updating business cards

We have already updated our logo via Pixel Forum and downloaded it (hopefully) for you to use. Now an updated set of business cards for Neil Pollard and Stuart Pollard are also needed... we are also hoping that a copy of our outdated business card designs have uploaded successfully as Microsoft Publisher files. Our Strength Through Unity motto has died a slow death so we are hoping to remove it (and other superfluous lingo if the graphic covers the idea) and instead opt for a fancy graphic (?) on the second side of the card that really reflects our desire to obtain product / haulage from Road Transport / Yard Operators and convert legs of their haulage to rail freight where profitable (bulk haulage / containterised etc). Can you help us look larger, bolder and more robust than we really are (two man show)?
Target Market(s)
Transport Industry
Industry/Entity Type
Business
Contact Information for Business Card
Card details for both N Pollard and S Pollard have been uploaded on the publisher files
Colors
Designer to choose colors to be used in the design.
Requirements
Must have
- Similar theme both sides of card
Should not have
- Black on one side white on the other

```html
<!DOCTYPE html>
<html lang="en">
<head>
<meta charset="utf-8">
<title>Ralton Freight – Business Cards</title>
<link rel="stylesheet" href="https://fonts.googleapis.com/css2?family=Roboto:wght@400;500;700&display=swap">
<style>
  :root {
    --backdrop: #4e4039;
    --card-light: #ffffff;
    --card-deep-start: #0f2f3a;
    --card-deep-end: #1a4b58;
    --teal: #1f87a0;
    --gold: #d4a23a;
    --text-grey: #4a4a4a;
    --text-dark: #333333;
    --text-light: #f2f2f2;
  }
  * { box-sizing: border-box; margin: 0; padding: 0; }
  html, body { width: 1200px; height: 1200px; overflow: hidden; }
  body {
    background: var(--backdrop);
    font-family: "Roboto", Arial, sans-serif;
    position: relative;
  }
  .card {
    position: absolute;
    left: 214px;
    width: 773px;
    height: 441px;
    box-shadow: 0 4px 14px rgba(0,0,0,0.35);
    overflow: hidden;
  }
  .card--front { top: 150px; background: var(--card-light); }
  .card--back {
    top: 633px;
    background: linear-gradient(135deg, var(--card-deep-start), var(--card-deep-end));
  }

  .brand {
    position: absolute;
    display: flex;
    align-items: center;
    gap: 10px;
    font-weight: 700;
    white-space: nowrap;
    transform: translate(-50%, -50%);
  }
  .brand__dot { border-radius: 50%; flex: none; }
  .card--front .brand { left: 204px; top: 220px; font-size: 38px; color: var(--teal); }
  .card--front .brand__dot { width: 16px; height: 16px; background: var(--teal); }
  .card--back .brand { left: 386px; top: 168px; font-size: 68px; color: var(--text-light); }
  .card--back .brand__dot { width: 28px; height: 28px; background: var(--gold); }

  .road-rail-graphic {
    position: absolute;
    left: 0; right: 0;
    top: 262px; height: 70px;
    background: linear-gradient(90deg, var(--gold) 0%, #8fa54a 45%, var(--teal) 100%);
    opacity: 0.85;
  }

  .divider {
    position: absolute;
    left: 388px; top: 97px;
    width: 2px; height: 247px;
    background: linear-gradient(to bottom, var(--teal), var(--gold));
  }
  .details { position: absolute; left: 424px; top: 0; right: 0; height: 100%; }
  .details > * { position: absolute; left: 0; white-space: nowrap; }
  .person-name { top: 90px; font-size: 29px; font-weight: 700; color: var(--teal); letter-spacing: 0.3px; }
  .person-role { top: 126px; font-size: 20px; color: var(--text-grey); }
  .address { top: 174px; font-size: 19px; line-height: 25px; color: var(--text-grey); }
  .contact { display: flex; align-items: center; gap: 8px; color: var(--text-dark); }
  .contact svg { flex: none; }
  .contact--phone { top: 240px; font-size: 19px; font-weight: 700; }
  .contact--email { top: 269px; font-size: 19px; font-weight: 700; }
  .contact--alt1 { top: 299px; font-size: 16px; }
  .contact--alt2 { top: 326px; font-size: 16px; }

  .website {
    position: absolute;
    left: 0; right: 0; top: 384px;
    text-align: center;
    font-size: 21px;
    color: var(--text-light);
  }
</style>
</head>
<body>
  <section class="card card--front">
    <div class="brand"><span class="brand__dot"></span>Ralton Freight</div>
    <div class="divider"></div>
    <div class="details">
      <h1 class="person-name">STUART POLLARD</h1>
      <p class="person-role">Director</p>
      <p class="address">14 Carrow Road<br>Dunmore NSW 2799</p>
      <p class="contact contact--phone">
        <svg width="12" height="18" viewBox="0 0 12 18"><rect x="1" y="1" width="10" height="16" rx="1.5" fill="none" stroke="#d4a23a" stroke-width="1.6"/><line x1="4.5" y1="14" x2="7.5" y2="14" stroke="#d4a23a" stroke-width="1.4"/></svg>
        0400 555 192
      </p>
      <p class="contact contact--email">
        <svg width="16" height="12" viewBox="0 0 16 12"><rect x="0.8" y="0.8" width="14.4" height="10.4" fill="none" stroke="#d4a23a" stroke-width="1.4"/><polyline points="1,1 8,7 15,1" fill="none" stroke="#d4a23a" stroke-width="1.4"/></svg>
        pollards@raltonfreight.com.au
      </p>
      <p class="contact contact--alt1">
        <svg width="16" height="12" viewBox="0 0 16 12"><rect x="0.8" y="0.8" width="14.4" height="10.4" fill="none" stroke="#d4a23a" stroke-width="1.4"/><polyline points="1,1 8,7 15,1" fill="none" stroke="#d4a23a" stroke-width="1.4"/></svg>
        raltonfreight@mailbox.com (Alternate)
      </p>
      <p class="contact contact--alt2">
        <svg width="16" height="12" viewBox="0 0 16 12"><rect x="0.8" y="0.8" width="14.4" height="10.4" fill="none" stroke="#d4a23a" stroke-width="1.4"/><polyline points="1,1 8,7 15,1" fill="none" stroke="#d4a23a" stroke-width="1.4"/></svg>
        raltonfreight@inbox.com (Alternate)
      </p>
    </div>
  </section>

  <section class="card card--back">
    <div class="brand"><span class="brand__dot"></span>Ralton Freight</div>
    <div class="road-rail-graphic" role="img" aria-label="Graphic of road haulage lanes merging into a rail freight line"></div>
    <p class="website">www.raltonfreight.com.au</p>
  </section>
</body>
</html>
```